Brightwell Homes Guide Business card

I have had at the logo designed here and attached. The business compares off the plan apartments in Sydney and provides quick comparison for new home buyers e.g price, floor plans and location. I would like the complimentary colours used on the business card. I would like it be unique but also look professional. I also have a website to gain inspiration from www.brightwellhomesguide.com.au
Updates
Industry/Entity Type
Business
Contact Information for Business Card
Helen Vostrakis
Director of Business Development
e: helen.vostrakis@brightwellhomesguide.com.au
p: (02) 8143 7692
m: 0431 572 908
w: www.brightwellhomesguide.com.au
Look and feel
Each slider illustrates characteristics of the customer's brand and the style your logo design should communicate.

```html
<!DOCTYPE html>
<html lang="en">
<head>
<meta charset="utf-8">
<title>Brightwell Homes Guide – Business Card</title>
<link rel="stylesheet" href="https://fonts.googleapis.com/css2?family=Lato:wght@400;700;900&display=swap">
<style>
  :root {
    --backdrop: #2b2b2b;
    --card-blue: #0b94d6;
    --card-blue-light: #2aa7e3;
    --card-white: #ffffff;
    --brand-green: #6ab42d;
    --brand-blue: #1b8fd3;
    --ink: #333333;
    --web-dark: #0b3a55;
    --accent-orange: #e8552b;
  }
  * { margin: 0; padding: 0; box-sizing: border-box; }
  html, body { width: 1200px; height: 873px; overflow: hidden; }
  body {
    background: var(--backdrop);
    font-family: "Lato", sans-serif;
    position: relative;
  }
  .card {
    position: absolute;
    top: 283px;
    width: 540px;
    height: 308px;
    border-radius: 18px;
    overflow: hidden;
  }
  .card--front {
    left: 40px;
    background: linear-gradient(160deg, var(--card-blue-light), var(--card-blue));
  }
  .card--back {
    left: 620px;
    background: var(--card-white);
  }
  .brand {
    display: flex;
    align-items: center;
    gap: 10px;
  }
  .brand__square {
    width: 26px;
    height: 26px;
    background: var(--brand-green);
  }
  .brand__name {
    font-weight: 700;
    font-size: 30px;
    color: var(--brand-green);
    letter-spacing: -0.3px;
    white-space: nowrap;
  }
  .card--front .brand {
    position: absolute;
    left: 40px;
    bottom: 74px;
  }
  .card--front .brand__square { background: var(--card-white); }
  .card--front .brand__name { color: var(--card-white); }
  .front__web {
    position: absolute;
    left: 42px;
    bottom: 46px;
    font-size: 13px;
    font-weight: 700;
    letter-spacing: 2.4px;
    color: var(--web-dark);
  }
  .card--back .brand {
    position: absolute;
    top: 46px;
    left: 0;
    right: 0;
    justify-content: center;
  }
  .person {
    position: absolute;
    left: 18px;
    top: 146px;
    width: 172px;
    text-align: right;
  }
  .person__name {
    font-weight: 900;
    font-size: 18px;
    color: var(--brand-green);
    white-space: nowrap;
  }
  .person__role {
    font-size: 13px;
    line-height: 1.3;
    color: var(--ink);
    margin-top: 3px;
  }
  .person__address {
    margin-top: 18px;
    font-weight: 900;
    font-size: 14px;
    line-height: 1.35;
    color: var(--brand-blue);
  }
  .divider {
    position: absolute;
    left: 204px;
    top: 140px;
    width: 3px;
    height: 115px;
    background: linear-gradient(to bottom, rgba(232,85,43,0), var(--accent-orange) 40%, rgba(232,85,43,0));
  }
  .contact {
    position: absolute;
    left: 222px;
    top: 138px;
    list-style: none;
  }
  .contact__item {
    display: flex;
    align-items: center;
    gap: 9px;
    font-size: 12px;
    color: var(--ink);
    height: 25px;
    white-space: nowrap;
  }
  .contact__icon { width: 14px; height: 14px; flex: none; }
</style>
</head>
<body>

<section class="card card--front" aria-label="Card front">
  <div class="brand">
    <span class="brand__square"></span>
    <span class="brand__name">Brightwell Homes Guide</span>
  </div>
  <p class="front__web">www.brightwellhomesguide.com.au</p>
</section>

<section class="card card--back" aria-label="Card back">
  <div class="brand">
    <span class="brand__square"></span>
    <span class="brand__name">Brightwell Homes Guide</span>
  </div>

  <div class="person">
    <p class="person__name">Helen Vostrakis</p>
    <p class="person__role">Director of Business Development</p>
    <p class="person__address">52 Larkfield Road,<br>Harbourvale NSW 2099</p>
  </div>

  <span class="divider"></span>

  <ul class="contact">
    <li class="contact__item">
      <svg class="contact__icon" viewBox="0 0 16 16"><path fill="#6ab42d" d="M3 2h3l1 3-2 1a8 8 0 0 0 5 5l1-2 3 1v3c0 1-1 1-1 1A12 12 0 0 1 2 3s0-1 1-1z"/></svg>
      (02) 8143 7692
    </li>
    <li class="contact__item">
      <svg class="contact__icon" viewBox="0 0 16 16"><rect x="5" y="1" width="6" height="14" rx="1.5" fill="#6ab42d"/><rect x="6.5" y="3" width="3" height="8" fill="#fff"/></svg>
      0431 572 908
    </li>
    <li class="contact__item">
      <svg class="contact__icon" viewBox="0 0 16 16"><rect x="1" y="3" width="14" height="10" fill="#6ab42d"/><path d="M1 3l7 6 7-6" fill="none" stroke="#fff" stroke-width="1.3"/></svg>
      helen.vostrakis@brightwellhomesguide.com.au
    </li>
    <li class="contact__item">
      <svg class="contact__icon" viewBox="0 0 16 16"><g fill="none" stroke="#6ab42d" stroke-width="2" stroke-linecap="round"><path d="M7 9l-2 2a2 2 0 0 1-3-3l2-2"/><path d="M9 7l2-2a2 2 0 0 1 3 3l-2 2"/><path d="M6 10l4-4"/></g></svg>
      www.brightwellhomesguide.com.au
    </li>
  </ul>
</section>

</body>
</html>
```